Nine Willows Bar and Grill Menu 2016

Our property is currently going through a renovation to modernize the look and feel of the unit. Nine Willows is a restaurant attached to a Halvorsen branded hotel in WI and we are making changes as well to provide a gathering place for both guests inside and outside of the hotel.
We need a new menu layout to help attract the local market for our restaurant. We are going for hip and trendy, easy to read, with a layout that is different from the normal fold that is seen everywhere. I have included the logo
Attached is a menu we really like to help give an idea of our style

Target Market(s)

25-45yr old

Industry/Entity Type

American Restaurant

Other font styles liked:
• Isabel Bold

Colors
1b1b1b
ec1f27
ffffff
d5d5d5

Requirements
Must have
• Must have multiple pages, bold fonts, and easy to change out pages if necessary
• photo on the front for a fun bar and grill type feel
• Menu included with page breaks
Nice to have
• bold headers for each category
• fun tag lines for each category
Should not have
• many pictures aside from the front and back pages of the menu

```html
<!DOCTYPE html>
<html lang="en">
<head>
<meta charset="utf-8">
<title>Nine Willows Bar and Grill – Menu</title>
<link href="https://fonts.googleapis.com/css2?family=Abril+Fatface&family=Alfa+Slab+One&family=Josefin+Sans:wght@600;700&family=Montserrat:wght@500;600&family=Rye&family=Yesteryear&family=Sancreek&display=swap" rel="stylesheet">
<style>
:root{
  --board:#1b1b1b;
  --board-light:#2a2a2a;
  --ink:#ffffff;
  --ink-soft:#d5d5d5;
  --accent:#ec1f27;
  --backdrop:#f2f2f2;
}
*{margin:0;padding:0;box-sizing:border-box}
html,body{width:1200px;height:624px;overflow:hidden;background:var(--backdrop)}
.spread{position:relative;width:1200px;height:624px}
.page{position:absolute;top:52px;width:370px;height:525px;color:var(--ink);overflow:hidden;
  background:radial-gradient(ellipse at 50% 40%,var(--board-light),var(--board) 75%);
  box-shadow:0 2px 6px rgba(0,0,0,.35);font-family:"Montserrat",sans-serif}
.page--appetizers{left:27px}
.page--salads{left:415px}
.page--entrees{left:803px}
.brand{position:absolute;left:121px;top:14px;width:96px;height:42px;display:flex;align-items:center;justify-content:center;gap:5px;
  border:1.5px solid var(--accent)}
.brand-mark{width:7px;height:7px;background:var(--accent)}
.brand-name{font-family:"Josefin Sans",sans-serif;font-weight:700;font-size:12px;color:var(--ink);letter-spacing:.5px;text-transform:uppercase}
.section-title{position:absolute;top:78px;left:0;width:100%;text-align:center;font-family:"Josefin Sans",sans-serif;font-weight:700;font-size:12px;letter-spacing:3px;text-transform:uppercase}
.section-title--wide{letter-spacing:6px}
.dish{position:absolute}
.dish-head{display:block;white-space:nowrap}
.dish-head--center{text-align:center}
.dish-head--indent{padding-left:24px}
.dish-name{display:block;line-height:.95;color:var(--ink)}
.slab{font-family:"Alfa Slab One",serif}
.rye{font-family:"Rye",serif}
.script{font-family:"Yesteryear",cursive;line-height:1}
.fat{font-family:"Abril Fatface",serif}
.western{font-family:"Sancreek",serif}
.dish-sub{font-family:"Josefin Sans",sans-serif;font-weight:700;letter-spacing:2px;display:block;line-height:1.2}
.dish-info{display:flex;gap:8px;margin-top:6px;align-items:flex-start}
.price{font-size:6px;font-weight:600;min-width:16px;text-align:right;flex:none}
.desc{font-size:4.3px;font-weight:600;letter-spacing:.3px;line-height:1.45;text-transform:uppercase;color:var(--ink-soft)}
.desc-strong{font-size:5.5px;color:var(--ink)}
.divider{position:absolute;left:185px;top:118px;width:1px;height:370px;background:var(--ink-soft);opacity:.6}
.extras{position:absolute;font-family:"Josefin Sans",sans-serif;font-weight:700;font-size:6.5px;letter-spacing:.8px;line-height:1.5;text-transform:uppercase}
.footnote{position:absolute;bottom:8px;left:0;width:100%;text-align:center;font-size:4.5px;font-weight:600;letter-spacing:.6px;text-transform:uppercase;color:var(--ink-soft)}
</style>
</head>
<body>
<main class="spread">

  <section class="page page--appetizers">
    <div class="brand"><span class="brand-mark"></span><span class="brand-name">Nine Willows</span></div>
    <h2 class="section-title section-title--wide">Appetizers</h2>

    <article class="dish" style="left:6px;top:115px;width:172px">
      <div class="dish-head dish-head--indent"><span class="dish-name rye" style="font-size:16px">BRUSCHETTA</span></div>
      <div class="dish-info"><span class="price">9</span><span class="desc">Tomato, basil, garlic, olive oil, parmesan cheese, parmesan crostinis | w/ shrimp 14</span></div>
    </article>

    <article class="dish" style="left:6px;top:178px;width:172px">
      <div class="dish-head dish-head--indent"><span class="dish-name slab" style="font-size:15px;line-height:1.1">SPINACH &amp;<br>ARTICHOKE DIP</span></div>
      <div class="dish-info"><span class="price">9</span><span class="desc">Spinach, artichoke, parmesan, garlic, jalapeño, cilantro, pico de gallo, house-made, crispy tortilla chips</span></div>
    </article>

    <article class="dish" style="left:6px;top:276px;width:172px">
      <div class="dish-head dish-head--center" style="padding-left:12px">
        <span class="dish-name script" style="font-size:22px">Crunchy</span>
        <span class="dish-name fat" style="font-size:27px">CHICKEN</span>
        <span class="dish-sub" style="font-size:11px;letter-spacing:3px">FINGERS</span>
      </div>
      <div class="dish-info"><span class="price">10</span><span class="desc">Hand breaded, deep fried</span></div>
    </article>

    <article class="dish" style="left:6px;top:388px;width:172px">
      <div class="dish-head dish-head--center" style="padding-left:12px">
        <span class="dish-name western" style="font-size:16px">SMOKED</span>
        <span class="dish-name slab" style="font-size:22px">WINGS</span>
      </div>
      <div class="dish-info"><span class="price">11</span><span class="desc">Buffalo, barbecue, szechwan or en fuego<br><span class="desc-strong">Boneless 10 | Traditional 11</span></span></div>
    </article>

    <article class="dish" style="left:184px;top:134px;width:170px">
      <div class="dish-head dish-head--center" style="padding-left:16px">
        <span class="dish-name rye" style="font-size:28px">CHICKEN</span>
        <span class="dish-sub" style="font-size:11px;letter-spacing:5px">NACHOS</span>
      </div>
      <div class="dish-info"><span class="price">11</span><span class="desc">Grilled chicken, queso, black beans, jalapeño, cilantro, pico de gallo, guacamole, sour cream, tortilla chips</span></div>
    </article>

    <article class="dish" style="left:184px;top:224px;width:170px">
      <div class="dish-head dish-head--center" style="padding-left:16px">
        <span class="dish-name script" style="font-size:19px">Crunchy</span>
        <span class="dish-name fat" style="font-size:18px">vegetables</span>
        <span class="dish-sub" style="font-size:8.5px">FLATBREADS</span>
      </div>
      <div class="dish-info"><span class="price">11</span><span class="desc">Fresh spinach &amp; artichoke sauce, tomato, mushrooms, basil, balsamic onions, mozzarella and provolone cheese blend</span></div>
    </article>

    <article class="dish" style="left:184px;top:322px;width:170px">
      <div class="dish-head dish-head--center" style="padding-left:16px">
        <span class="dish-name western" style="font-size:17px">BUFFALO</span>
        <span class="dish-name rye" style="font-size:27px">CHICKEN</span>
        <span class="dish-sub" style="font-size:8.5px">FLATBREADS</span>
      </div>
      <div class="dish-info"><span class="price">11.50</span><span class="desc">Grilled chicken, green onion, blue cheese crumbles, buffalo sauce, smoked onion ranch, mozzarella and provolone</span></div>
    </article>

    <p class="footnote">An 18% service charge will be added to all purchases for parties of 8 or more.</p>
  </section>

  <section class="page page--salads">
    <div class="brand"><span class="brand-mark"></span><span class="brand-name">Nine Willows</span></div>
    <h2 class="section-title">Salads • Soups • Lettuce Wraps</h2>
    <div class="divider"></div>

    <article class="dish" style="left:8px;top:118px;width:172px">
      <div class="dish-head dish-head--center" style="padding-left:12px"><span class="dish-name rye" style="font-size:13px;line-height:1.05">PEAR AND<br>BLUE CHEESE</span></div>
      <div class="dish-info"><span class="price">9</span><span class="desc">Field greens, blue cheese crumbles, dried cranberries, candied pecans, balsamic glaze, apple cider vinaigrette</span></div>
    </article>

    <article class="dish" style="left:8px;top:180px;width:172px">
      <div class="dish-head dish-head--center" style="padding-left:12px">
        <span class="dish-name script" style="font-size:19px">Classic</span>
        <span class="dish-name slab" style="font-size:20px">CAESAR</span>
      </div>
      <div class="dish-info"><span class="price">8.50</span><span class="desc">Romaine, parmesan, croutons</span></div>
    </article>

    <article class="dish" style="left:8px;top:250px;width:172px">
      <div class="dish-head dish-head--center" style="padding-left:12px">
        <span class="dish-name rye" style="font-size:26px">CHOP</span>
        <span class="dish-name rye" style="font-size:26px">SALAD</span>
      </div>
      <div class="dish-info"><span class="price">9.50</span><span class="desc">Iceberg lettuce, bacon, tomato, avocado, carrot, blue cheese crumbles, onion, garbanzo beans, egg, cucumber, tortilla strips, house vinaigrette</span></div>
    </article>

    <article class="dish" style="left:8px;top:350px;width:172px">
      <div class="dish-head dish-head--center" style="padding-left:12px"><span class="dish-name fat" style="font-size:22px">BLT WEDGE</span></div>
      <div class="dish-info"><span class="price">9</span><span class="desc">Iceberg lettuce, bacon, bruschetta, green onion, egg, blue cheese crumbles, ranch</span></div>
    </article>

    <div class="extras" style="left:40px;top:426px">Add on protein options:<br>&nbsp;&nbsp;Chicken 4<br>&nbsp;&nbsp;Shrimp &nbsp;5<br>&nbsp;&nbsp;Salmon &nbsp;6</div>

    <article class="dish" style="left:190px;top:140px;width:165px">
      <div class="dish-head dish-head--center" style="padding-left:12px">
        <span class="dish-name script" style="font-size:13px">Sesame</span>
        <span class="dish-name rye" style="font-size:18px">CHICKEN</span>
        <span class="dish-sub" style="font-size:6.5px">LETTUCE WRAPS</span>
      </div>
      <div class="dish-info"><span class="price">11</span><span class="desc">Seared sesame chicken, green onion, yellow onion, red pepper, cilantro, carrot, water chestnuts, ginger and soy sauce, served with romaine lettuce cups, sweet thai chili and dijon mustard sauces</span></div>
    </article>

    <article class="dish" style="left:190px;top:224px;width:165px">
      <div class="dish-head dish-head--center" style="padding-left:12px">
        <span class="dish-name western" style="font-size:12px">GINGER</span>
        <span class="dish-name rye" style="font-size:18px">CHICKEN</span>
        <span class="dish-sub" style="font-size:6.5px">LETTUCE WRAPS</span>
      </div>
      <div class="dish-info"><span class="price">12</span><span class="desc">Sautéed shrimp, green onion, yellow onion, red pepper, cilantro, carrot, water chestnuts, ginger and soy sauce, served with romaine lettuce cups, sweet thai chili and dijon mustard sauces</span></div>
    </article>

    <article class="dish" style="left:190px;top:310px;width:165px">
      <div class="dish-head dish-head--center" style="padding-left:12px">
        <span class="dish-name script" style="font-size:13px">Jerk</span>
        <span class="dish-name rye" style="font-size:12px">CHICKEN &amp; SHRIMP</span>
        <span class="dish-sub" style="font-size:6.5px">LETTUCE WRAPS</span>
      </div>
      <div class="dish-info"><span class="price">12</span><span class="desc">Seared chicken and sautéed shrimp, jalapeño, yellow onion, red pepper, carrot, pineapple, cilantro, rice sticks, ginger and soy sauce, served with romaine lettuce cups, barbecue and chili sambal sauce</span></div>
    </article>

    <div class="extras" style="left:205px;top:426px">Baked French onion 5 /<br>Chefs choice soup of the day 4</div>

    <p class="footnote">An 18% service charge will be added to all purchases for parties of 8 or more.</p>
  </section>

  <section class="page page--entrees">
    <div class="brand"><span class="brand-mark"></span><span class="brand-name">Nine Willows</span></div>
    <h2 class="section-title">Entrees • Plates</h2>

    <article class="dish" style="left:95px;top:122px;width:180px">
      <div class="dish-head dish-head--center"><span class="dish-name rye" style="font-size:17px">FISH &amp; CHIPS</span></div>
      <div class="dish-info"><span class="price">13.50</span><span class="desc">Beer-battered fish, tartar sauce, fries</span></div>
    </article>

    <article class="dish" style="left:95px;top:164px;width:180px">
      <div class="dish-head dish-head--center">
        <span class="dish-name script" style="font-size:16px">Tuscan</span>
        <span class="dish-name fat" style="font-size:21px">CHICKEN</span>
        <span class="dish-name script" style="font-size:16px">pasta</span>
      </div>
      <div class="dish-info"><span class="price">13.50</span><span class="desc">Grilled chicken, artichoke, cavatappi noodles, fresh spinach, three-cheese blend, basil, tomato, mushrooms, alfredo sauce</span></div>
    </article>

    <article class="dish" style="left:95px;top:252px;width:180px">
      <div class="dish-head dish-head--center">
        <span class="dish-name script" style="font-size:19px">Lemon</span>
        <span class="dish-name fat" style="font-size:21px">CHICKEN</span>
      </div>
      <div class="dish-info"><span class="price">12.50</span><span class="desc">Lemon-parmesan breaded chicken, alfredo sauce, sautéed vegetables, rice pilaf</span></div>
    </article>

    <article class="dish" style="left:95px;top:326px;width:180px">
      <div class="dish-head dish-head--center">
        <span class="dish-name script" style="font-size:16px">Spicy</span>
        <span class="dish-name slab" style="font-size:15px">Pasta</span>
      </div>
      <div class="dish-info"><span class="price">14</span><span class="desc">Shrimp, andouille sausage, cavatappi noodles, yellow onion, green and red pepper, garlic, chili sambal sauce, alfredo sauce, parmesan, parsley</span></div>
    </article>

    <article class="dish" style="left:95px;top:404px;width:180px">
      <div class="dish-head dish-head--center">
        <span class="dish-name script" style="font-size:16px">Baked</span>
        <span class="dish-name slab" style="font-size:16px">MAC &amp; CHEESE</span>
      </div>
      <div class="dish-info"><span class="price">10.50</span><span class="desc">Custom four cheese blend, macaroni, baked golden<br>w/broccoli, bacon or jalapeño 12 &nbsp;w/grilled or fried chicken 14<br>w/shrimp 15</span></div>
    </article>

    <p class="footnote">An 18% service charge will be added to all purchases for parties of 8 or more.</p>
  </section>

</main>
</body>
</html>
```